Car rental website design for a UAE car rental company

This project is about creating a new website design for a car rental company located in Dubai (United Arab Emirates), I opened the same project a few months ago but I didn't receive a lot of appealing entries so I closed it but this time I am marking the project as guaranteed to avoid such situation again, if you have already provided a design before then please re-submit again on this project so that it is considered while reviewing all the designs

A few important things:

1- We need a simple non-complex design
2- The final deliverable would be 2 screens (PSD, JPEG ... etc), the first screen is for the home page and the second screen is for an internal page
3- The home page must have a section that end users can use to rent a car online directly from the home page instead of going into some inner pages
4- The current website is very old and not very appealing so avoid creating a similar design (www.quarvin-drive.example)
5- The name is Quarvin but the company rents normal cars (no Limousin cars will be rented) so avoid adding any fancy cars in the images/graphics used in the design, just normal end users cars
6- The expected pages would be: home, About us, Our team, Strategy, Contact us and links to social media pages
7- The attachments include the company's logo and some screens from other car rental companies that provide online rentals/payments

If you have any questions please feel free to ask and please note that we will need the designs urgently

Thanks

Target Market(s)

Dubai - United Arab Emirates

Industry/Entity Type

It Company

Number of Pages Required

2 page

Font styles to use
Sans Serif

Requirements
Must have
• Check the project details
Nice to have
Should not have

```html
<!DOCTYPE html>
<html lang="en">
<head>
<meta charset="utf-8">
<title>Quarvin Rent A Car</title>
<link href="https://fonts.googleapis.com/css2?family=Open+Sans:wght@400;600;700&family=Crimson+Text:wght@400;600&display=swap" rel="stylesheet">
<style>
:root{
  --magenta:#c8134a;
  --magenta-dark:#a3063a;
  --wine:#9c0a3c;
  --grey-text:#6b6b6b;
  --dark:#222;
  --sage:#8c9a90;
  --panel:#e6e6e6;
  --line:#cfcfcf;
  --white:#fff;
}
*{margin:0;padding:0;box-sizing:border-box}
html,body{width:1200px;height:1012px;overflow:hidden;background:var(--white)}
body{position:relative;font-family:"Open Sans",Arial,sans-serif;color:var(--dark)}
.abs{position:absolute}
.top-rule{left:0;top:0;width:1200px;height:4px;background:#8e8e8e}
.brand{left:169px;top:34px;display:flex;align-items:center;gap:14px}
.brand-mark{width:50px;height:50px;border:3px solid var(--wine);background:#6b6b6b}
.brand-name{font-size:32px;font-weight:600;color:#7a7a7a;letter-spacing:.5px}
.call{left:824px;top:34px;display:flex;align-items:center;gap:10px}
.call-text small{display:block;font-size:16px;color:#333;line-height:1.1}
.call-text strong{font-size:24px;font-weight:600;color:#222;line-height:1.1}
.nav{left:0;top:116px;width:1200px;height:43px;background:linear-gradient(#d8295a,var(--magenta) 50%,var(--magenta-dark));}
.nav a{position:absolute;top:10px;font-family:"Crimson Text",Georgia,serif;font-size:19px;color:var(--white);text-decoration:none;letter-spacing:.5px;white-space:nowrap}
.nav .div{position:absolute;top:0;width:1px;height:43px;background:rgba(0,0,0,.18);box-shadow:1px 0 rgba(255,255,255,.2)}
.social{position:absolute;top:8px;left:922px;display:flex;gap:6px}
.social span{width:25px;height:25px;border-radius:50%;background:#2b74b8;border:2px solid var(--white)}
.headline{left:0;top:198px;width:1200px;text-align:center;font-size:30px;line-height:33px;color:#111;font-weight:400}
.hero-img{left:36px;top:282px;width:1106px;height:212px;background:linear-gradient(90deg,#2b2b2b 0%,#bdbdbd 18%,#c8231f 30%,#2f6fd0 45%,#1d1d1d 60%,#e9e9e9 75%,#b4b8bd 95%);border-radius:40px 60px 30px 30px;opacity:.9}
.caption{left:153px;top:496px;width:892px;height:49px;background:#626262;color:var(--white);font-size:21px;padding:11px 14px;white-space:nowrap}
.dots{position:absolute;right:14px;top:20px;display:flex;gap:5px}
.dots i{width:7px;height:7px;border-radius:50%;background:#fff}
.dots i:first-child{background:#aaa}
.sep{left:0;top:546px;width:1200px;height:1px;background:var(--line)}
.card{top:593px;height:238px;border:1px solid #ddd;border-radius:4px;background:linear-gradient(#fafafa,#f0f0f0);padding:14px 14px}
.card h2{font-family:"Crimson Text",Georgia,serif;font-weight:400;font-size:40px;line-height:36px;color:var(--wine)}
.card h3{font-weight:400;font-size:16px;color:#333;margin-bottom:10px;letter-spacing:.3px}
.card p{font-size:10.5px;line-height:18px;color:#333;text-transform:uppercase}
.btn{position:absolute;left:16px;bottom:14px;width:110px;height:31px;background:var(--wine);color:#fff;font-size:12px;text-align:center;line-height:31px;border-radius:2px}
.search{left:166px;width:278px;background:var(--sage);border-color:#7d8a80}
.search h2{color:#2c2c2c}
.search h3{color:#2e2e2e}
.select{height:26px;background:#fff;border:1px solid #bbb;margin:0 6px 9px 2px;font-size:10px;color:#999;padding:6px 8px;position:relative}
.select::after{content:"";position:absolute;right:3px;top:3px;width:18px;height:18px;background:#ddd}
.search .btn{background:#1b1b1b}
.special{left:457px;width:285px}
.gift{left:750px;width:281px}
.contact{left:162px;top:863px;width:870px;height:91px;background:var(--panel);border:1px solid #d6d6d6;border-radius:4px}
.contact div{position:absolute;top:20px;white-space:nowrap}
.contact b{display:block;font-family:"Crimson Text",Georgia,serif;font-weight:400;font-size:19px;color:var(--wine)}
.contact span{font-size:11.5px;color:#777}
.footer{left:162px;top:969px;width:870px;height:26px;font-size:11px}
.footer-link{position:absolute;top:5px;color:#333;text-decoration:none;white-space:nowrap;line-height:16px}
.footer-link.current{color:var(--wine)}
.footer-div{position:absolute;top:5px;width:1px;height:16px;background:#ccc}
.ficons{position:absolute;left:455px;top:4px;display:flex;gap:4px}
.ficons i{width:17px;height:17px;border:1px solid #666;border-radius:50%}
.ficons i:first-child{border-color:var(--wine)}
.copy{position:absolute;right:0;top:5px;line-height:16px;color:#333;white-space:nowrap}
.bottom-rule{left:0;top:1003px;width:1200px;height:9px;background:var(--wine)}
</style>
</head>
<body>
<div class="abs top-rule"></div>
<div class="abs brand"><span class="brand-mark"></span><span class="brand-name">Quarvin</span></div>
<div class="abs call">
  <svg width="46" height="46" viewBox="0 0 46 46" aria-hidden="true"><circle cx="23" cy="23" r="21" fill="none" stroke="#a3063a" stroke-width="3"/><path d="M15 13c2-2 4-1 5 1l2 4c1 2 0 3-1 4 1 3 3 5 6 6 1-1 2-2 4-1l4 2c2 1 3 3 1 5-3 3-7 2-12-2s-8-10-9-13c-1-3 0-5 0-6z" fill="#a3063a"/></svg>
  <div class="call-text"><small>CALL US NOW:</small><strong>971 4 5550182</strong></div>
</div>
<nav class="abs nav">
  <a style="left:173px">HOME</a><span class="div" style="left:257px"></span>
  <a style="left:282px">ABOUT US</a><span class="div" style="left:398px"></span>
  <a style="left:424px">OUR TEAM</a><span class="div" style="left:549px"></span>
  <a style="left:581px">STRATEGY</a><span class="div" style="left:711px"></span>
  <a style="left:742px">CONTACT US</a>
  <div class="social"><span></span><span></span><span></span><span></span></div>
</nav>
<h1 class="abs headline">SED UT PERSPICIATIS UNDE<br>OMNIS ISTE NATUS ERROR SIT VOLUPTATEM</h1>
<div class="abs hero-img" role="img" aria-label="Row of everyday rental cars in black, white, red, blue and silver"></div>
<div class="abs caption">SED UT PERSPICIATIS UNDE OMNIS ISTE NATUS ERROR SIT VOLUPTATEM<div class="dots"><i></i><i></i><i></i><i></i></div></div>
<div class="abs sep"></div>

<section class="abs card search">
  <h2>SEARCH</h2><h3>CALCULATE AND BOOK</h3>
  <div class="select">ALL CAR TYPES</div>
  <div class="select">ALL CAR BRANDS</div>
  <div class="select">ALL CAR MODELS</div>
  <div class="btn" style="left:18px;width:110px">SEARCH NOW</div>
</section>
<section class="abs card special">
  <h2>SPECIAL</h2><h3>OFFERS &amp; PACKAGES</h3>
  <p>Lorem ipsum dolor sit amet conse ctedfitur dipis icing elit, sed do eiusmod tem dsfgsdfg ddpor incididunt ut labore et dvhffholore ddfhg dmagna aliqua. Ut ehjkhfgjhfjhf nim ad minim veniam.</p>
  <div class="btn">READ MORE</div>
</section>
<section class="abs card gift">
  <h2>GIFT</h2><h3>CERTIFICATES</h3>
  <p>Lorem ipsum dolor sit amet conse ctedfitur dipis icing elit, sed do eiusmod tem dsfgsdfg ddpor incididunt ut labore et dvhffholore ddfhg dmagna aliqua. Ut ehjkhfgjhfjhf nim ad minim veniam.</p>
  <div class="btn">READ MORE</div>
</section>

<div class="abs contact">
  <div style="left:16px"><b>ADDRESS:</b><span>P.O. Box 100240 Dubai, UAE, Tel: +971 4 5550182</span></div>
  <div style="left:318px"><b>PHONE:</b><span>+1(555) 014-2270; 971 4 5550182.</span></div>
  <div style="left:604px"><b>E-MAIL:</b><span>info@quarvin-drive.example</span></div>
</div>
<footer class="abs footer">
  <a class="footer-link current" style="left:0">HOME</a><span class="footer-div" style="left:45px"></span>
  <a class="footer-link" style="left:61px">ABOUT US</a><span class="footer-div" style="left:125px"></span>
  <a class="footer-link" style="left:142px">OUR TEAM</a><span class="footer-div" style="left:212px"></span>
  <a class="footer-link" style="left:230px">STRATEGY</a><span class="footer-div" style="left:297px"></span>
  <a class="footer-link" style="left:314px">CONTACT US</a>
  <span class="ficons"><i></i><i></i><i></i><i></i></span>
  <span class="copy">© 2015. <b>Quarvin Rent A Car.</b> All Rights Reserved.</span>
</footer>
<div class="abs bottom-rule"></div>
</body>
</html>
```